Legal Information Website

We need a website that will serve as a source of information for people visiting, living, and working in the United Arab Emirates, where they can go and read about legal issues, laws, crimes, and most important find legal advice and find lawyers. The following are the pages of the website:

Find a Lawyer (Home Page)
This main feature of this page should be "Find a Lawyer"
Find a Lawyer should include the searching option by practice, by lawyer’s name, by Meridian Law name or by location.

Ask a lawyer
This function allows the user to ask a lawyer a legal question and get an answer directly from a lawyer.

Research a legal matter
This function allows the user to do research on a certain legal topic. He/she can select from different legal topics.

Contact Us:
This page should include our contact details for the visitors in case they need any assistance. Contact us by Phone, Email, or Chat.

Once the design is approved, we will provide the rest of the website text.

Target Market(s)

General Public who seek legal advice

Industry/Entity Type

Meridian Law

Font styles to use
Serif
Sans Serif

Requirements
Must have
• A tool to search for lawyer's, and then display the lawyer's picture and profile and credentials.

```html
<!DOCTYPE html>
<html lang="en">
<head>
<meta charset="utf-8">
<title>Counsel Compass – Find a Lawyer</title>
<link rel="stylesheet" href="https://fonts.googleapis.com/css2?family=Josefin+Sans:wght@300;400;600&family=PT+Sans:wght@400;700&display=swap">
<style>
:root{
  --teal:#15958f;
  --teal-dark:#0f7f7a;
  --ink:#2b2b2b;
  --muted:#666;
  --header:#1b1b1b;
  --footer:#111;
  --hero-a:#cfd2d3;
  --hero-b:#9ea3a5;
  --band-a:#f4f4f4;
  --band-b:#e2e2e2;
  --white:#fff;
}
*{box-sizing:border-box;margin:0;padding:0}
html,body{width:778px;height:1200px;overflow:hidden;background:var(--white)}
body{position:relative;font-family:"PT Sans",sans-serif;color:var(--ink)}
.abs{position:absolute}
h1,h2,h3,h4{font-weight:300}

.site-header{left:0;top:0;width:778px;height:57px;background:var(--header)}
.brand{left:118px;top:18px;font-family:"Josefin Sans",sans-serif;font-weight:300;font-size:20px;line-height:22px;color:#cfcfcf;white-space:nowrap;display:flex;align-items:center;gap:8px}
.brand .dot{width:14px;height:14px;border-radius:50%;background:var(--teal)}
.main-nav{left:0;top:25px;width:600px;height:12px;font-family:"Josefin Sans",sans-serif;font-size:8.5px;color:#9a9a9a;letter-spacing:.3px;white-space:nowrap}
.main-nav span{position:absolute;top:0}
.main-nav .active{color:var(--teal)}
.social{display:flex;gap:5px}
.social span{width:17px;height:17px;border-radius:50%;background:var(--teal);display:block}
.header-social{left:605px;top:22px}

.hero{left:0;top:57px;width:778px;height:291px;background:linear-gradient(90deg,var(--hero-a),#dcdede 45%,var(--hero-b))}
.hero-photo{left:340px;top:57px;width:330px;height:291px;background:linear-gradient(180deg,#b9bcbd,#e9e7e3 40%,#c3b8ae)}
.hero-title{left:118px;top:106px;font-family:"Josefin Sans",sans-serif;font-weight:300;font-size:42px;line-height:40px;color:#333}
.hero-sub{left:121px;top:196px;font-family:"Josefin Sans",sans-serif;font-weight:300;font-size:22px;line-height:27px;color:#333}

.search-bar{left:111px;top:303px;width:555px;height:45px;background:var(--teal)}
.search-bar > *{position:absolute}
.search-bar .label{left:15px;top:17px;font-family:"Josefin Sans",sans-serif;font-size:11px;color:#fff;white-space:nowrap}
.field{top:15px;height:17px;background:#fff;font-size:9px;line-height:9px;color:#777;padding:4px 6px}
.field.select::after{content:"";position:absolute;right:6px;top:5px;border:4px solid transparent;border-top:5px solid #222}
.find-btn{left:447px;top:14px;width:95px;height:20px;border:1px solid #fff;color:#fff;font-family:"Josefin Sans",sans-serif;font-size:12px;display:flex;align-items:center;justify-content:center;gap:6px;white-space:nowrap}

.welcome{left:0;top:368px;width:778px;text-align:center;font-family:"Josefin Sans",sans-serif;font-weight:300;font-size:21px;color:#333;white-space:nowrap}
.welcome b{font-weight:300;color:var(--teal)}
.welcome-sub{left:0;top:399px;width:778px;text-align:center;font-family:"Josefin Sans",sans-serif;font-weight:300;font-size:12px;color:#555}

.intro-title{left:113px;top:440px;width:280px;font-family:"Josefin Sans",sans-serif;font-weight:300;font-size:15px;line-height:18px;color:#333}
.intro-text{left:113px;top:481px;width:280px;font-size:7.3px;line-height:12.2px;color:#444}
.video{left:408px;top:443px;width:255px;height:146px;background:linear-gradient(90deg,#6b4a2d,#a17a4f 60%,#d3a461);border:2px solid #222}
.play{left:513px;top:496px;width:44px;height:44px;border:3px solid rgba(255,255,255,.75);border-radius:50%}
.play::after{content:"";position:absolute;left:15px;top:9px;border:10px solid transparent;border-left:14px solid rgba(255,255,255,.8)}

.divider{left:60px;top:607px;width:660px;height:4px;background:radial-gradient(ellipse at center,rgba(0,0,0,.12),transparent 70%)}
.mission-title{left:0;top:624px;width:778px;text-align:center;font-family:"Josefin Sans",sans-serif;font-weight:300;font-size:22px;color:#333}
.mission-title b{font-weight:300;color:var(--teal)}
.mission-item{top:654px;width:140px;text-align:center}
.mission-item .icon{width:86px;height:86px;border-radius:50%;background:var(--teal);margin:0 auto}
.mission-item h3{font-family:"Josefin Sans",sans-serif;font-weight:300;font-size:15px;line-height:16px;margin-top:13px;color:#222}
.mission-item p{width:120px;margin:3px auto 0;font-size:7.3px;line-height:12.3px;color:#555}
.btn-outline{display:inline-block;border:1px solid var(--teal);font-family:"Josefin Sans",sans-serif;font-size:9px;line-height:9px;padding:3px 10px 2px;color:#333;margin-top:8px}

.cta-band{left:0;top:892px;width:778px;height:80px;background:linear-gradient(180deg,var(--band-b),var(--band-a) 50%,var(--band-b))}
.cta{top:907px;text-align:center}
.cta p{font-family:"Josefin Sans",sans-serif;font-size:12px;color:#333;white-space:nowrap}
.cta .btn{margin-top:5px;height:23px;border:2px solid var(--teal);background:#fff;color:var(--teal);font-family:"Josefin Sans",sans-serif;font-size:12px;display:flex;align-items:center;justify-content:center;white-space:nowrap}

.footer-col h4{font-family:"Josefin Sans",sans-serif;font-weight:400;font-size:10px;color:#222;letter-spacing:.3px;white-space:nowrap}
.footer-col ul{list-style:none;margin-top:9px;font-size:8.5px;line-height:14.5px;color:#444}
.contact-head{font-family:"Josefin Sans",sans-serif;font-size:12px;color:var(--teal)}
.contact-row{display:flex;align-items:center;gap:7px;font-size:9px;color:#333;white-space:nowrap}
.small{font-size:6px;line-height:8.5px;color:#333}
.form-field{width:143px;height:18px;background:#f1f1f1;border:1px solid #ddd;font-size:7.5px;color:#555;display:flex;align-items:center;gap:6px;padding-left:6px}
.send{width:50px;height:16px;border:1px solid var(--teal);font-family:"Josefin Sans",sans-serif;font-size:8px;display:flex;align-items:center;justify-content:center}

.site-footer{left:0;top:1140px;width:778px;height:60px;background:var(--footer)}
.copyright{left:126px;top:1161px;font-size:7.5px;color:#ddd;white-space:nowrap}
.copyright small{display:block;color:#888;font-size:6.5px;margin-top:4px}
.footer-social{left:360px;top:1157px}
.footer-brand{left:490px;top:1155px;font-family:"Josefin Sans",sans-serif;font-weight:300;font-size:20px;line-height:22px;color:#9a9a9a;white-space:nowrap;display:flex;align-items:center;gap:8px}
.footer-brand .dot{width:14px;height:14px;border-radius:50%;background:var(--teal)}
</style>
</head>
<body>

<header class="site-header abs"></header>
<div class="brand abs"><span class="dot"></span>COUNSEL COMPASS</div>
<nav class="main-nav abs">
  <span class="active" style="left:361px">HOME</span>
  <span style="left:409px">RIGHTS</span>
  <span style="left:457px">LAWYERS</span>
  <span style="left:511px">NEWS</span>
  <span style="left:553px">CONTACT</span>
</nav>
<div class="social header-social abs"><span></span><span></span><span></span></div>

<section class="hero abs"></section>
<div class="hero-photo abs" role="img" aria-label="Portrait photograph of a lawyer in traditional headdress and glasses"></div>
<h1 class="hero-title abs">NEED A<br>LAWYER</h1>
<p class="hero-sub abs">We’ll find the best<br>lawyer in town for you!</p>

<form class="search-bar abs">
  <span class="label">FIND A LAWYER</span>
  <div class="field" style="left:109px;width:99px">First Name</div>
  <div class="field select" style="left:214px;width:95px">City</div>
  <div class="field select" style="left:314px;width:120px">Area Of Practice</div>
  <div class="find-btn">
    <svg width="11" height="11" viewBox="0 0 12 12"><circle cx="5" cy="5" r="3.6" fill="none" stroke="#fff" stroke-width="1.6"/><line x1="7.6" y1="7.6" x2="11" y2="11" stroke="#fff" stroke-width="1.8"/></svg>
    FIND NOW!
  </div>
</form>

<h2 class="welcome abs">WELCOME TO THE <b>COUNSEL COMPASS WEBSITE</b></h2>
<p class="welcome-sub abs">Our Lawyers Helped Millions Of People Make Smarter, More Confident Legal Decisions.</p>

<h3 class="intro-title abs">Your No.1 search tool for the best lawyers in the country</h3>
<p class="intro-text abs">Lorem ipsum dolor sit amet, consectetuer adipiscing elit, sed diam nonummy nibh euismod tincidunt ut laoreet dolore magna aliquam erat volutpat.Lorem ipsum dolor sit amet, consectetuer adipiscing elit, sed diam nonummy nibh euismod tincidunt ut laoreet dolore magna aliquam erat volutpat.Lorem ipsum dolor sit amet, consectetuer adipiscing elit, sed diam nonummy nibh euismod tincidunt ut laoreet dolore magna aliquam erat volutpat.Lorem ipsum dolor sit amet, consectetuer adipiscing elit, sed diam nonummy nibh euismod tincidunt ut laoreet dolore magna aliquam erat volutpat.Lorem euismod tincidunt ut laoreet dolore magna aliquam erat volutpat.</p>
<div class="video abs" role="img" aria-label="Video still of a lawyer in a suit seated before bookshelves"></div>
<div class="play abs"></div>

<div class="divider abs"></div>
<h2 class="mission-title abs">OUR <b>MISSION</b></h2>

<div class="mission-item abs" style="left:101px">
  <div class="icon" role="img" aria-label="Lawyer pictogram"></div>
  <h3>LAWYER</h3>
  <p>Lorem ipsum dolor sit amet, consectetuer adipiscing elit, sed diam nonummy nibh euismod tincidunt ut laoreet dolore magna aliquam erat volutpat.</p>
  <span class="btn-outline">READ MORE</span>
</div>
<div class="mission-item abs" style="left:243px">
  <div class="icon" role="img" aria-label="Handshake meeting pictogram"></div>
  <h3>MEETING</h3>
  <p>Lorem ipsum dolor sit amet, consectetuer adipiscing elit, sed diam nonummy nibh euismod tincidunt ut laoreet dolore magna aliquam erat volutpat.</p>
  <span class="btn-outline">READ MORE</span>
</div>
<div class="mission-item abs" style="left:389px">
  <div class="icon" role="img" aria-label="Gavel pictogram"></div>
  <h3>JUSTICE</h3>
  <p>Lorem ipsum dolor sit amet, consectetuer adipiscing elit, sed diam nonummy nibh euismod tincidunt ut laoreet dolore magna aliquam erat volutpat.</p>
  <span class="btn-outline">READ MORE</span>
</div>
<div class="mission-item abs" style="left:533px">
  <div class="icon" role="img" aria-label="Scales pictogram"></div>
  <h3>EQUALITY</h3>
  <p>Lorem ipsum dolor sit amet, consectetuer adipiscing elit, sed diam nonummy nibh euismod tincidunt ut laoreet dolore magna aliquam erat volutpat.</p>
  <span class="btn-outline">READ MORE</span>
</div>

<section class="cta-band abs"></section>
<div class="cta abs" style="left:127px;width:143px"><p>Have An Urgent Problem?</p><div class="btn">Find a Lawyer</div></div>
<div class="cta abs" style="left:312px;width:157px"><p>Looking For Information?</p><div class="btn">Research Legal Advice</div></div>
<div class="cta abs" style="left:513px;width:140px"><p>Didn’t Find An Answer?</p><div class="btn">Ask a Lawyer</div></div>

<div class="footer-col abs" style="left:126px;top:993px;width:140px">
  <h4>TALK TO OUR TEAM</h4>
  <div class="contact-head" style="margin-top:9px">Give us a call:</div>
  <div class="contact-row" style="margin-top:6px">
    <svg width="11" height="11" viewBox="0 0 12 12"><path d="M2 1l2.3 0 1 3-1.5 1a6 6 0 0 0 3.2 3.2l1-1.5 3 1V11A9.5 9.5 0 0 1 1 2z" fill="var(--teal)"/></svg>555-014-2290
  </div>
  <div class="contact-row" style="margin-top:11px">
    <svg width="11" height="8" viewBox="0 0 11 8"><rect width="11" height="8" fill="var(--teal)"/><path d="M0 0l5.5 4.5L11 0" fill="none" stroke="#fff" stroke-width="1"/></svg>info@counselcompass.com
  </div>
  <div class="contact-head" style="margin-top:11px">Office Address:</div>
  <p class="small" style="margin-top:4px;width:120px">Lorem ipsum dolor sit amet, consectetuer adipiscing elit, sed diam nonummy nibh euismod</p>
</div>

<div class="footer-col abs" style="left:281px;top:993px">
  <h4>WHO WE ARE</h4>
  <ul><li>About</li><li>Your Team</li><li>Our Process</li><li>Blog</li><li>Hosting Network</li><li>Join our focus group</li></ul>
</div>
<div class="footer-col abs" style="left:394px;top:993px">
  <h4>FIND ANSWERS</h4>
  <ul><li>FAQs</li><li>Library</li><li>Glossary</li></ul>
</div>
<div class="footer-col abs" style="left:515px;top:993px">
  <h4>SEND US A MESSAGE</h4>
  <div class="form-field" style="margin-top:9px">
    <svg width="8" height="8" viewBox="0 0 8 8"><circle cx="4" cy="2.3" r="2" fill="var(--teal)"/><path d="M0 8a4 3.5 0 0 1 8 0z" fill="var(--teal)"/></svg>Name</div>
  <div class="form-field" style="margin-top:3px">
    <svg width="9" height="6" viewBox="0 0 9 6"><rect width="9" height="6" fill="var(--teal)"/></svg>Email</div>
  <div class="form-field" style="margin-top:3px;height:47px;align-items:flex-start;padding-top:5px">
    <svg width="9" height="7" viewBox="0 0 9 7"><path d="M0 0h9v5H3L1 7V5H0z" fill="var(--teal)"/></svg>Message</div>
  <div class="send" style="margin-left:91px;margin-top:4px">SEND</div>
</div>

<footer class="site-footer abs"></footer>
<p class="copyright abs">Copyright © 2014 MERIDIAN LAW. All Rights Reserved<small>Sitemap &nbsp;&nbsp; Privacy</small></p>
<div class="social footer-social abs"><span></span><span></span><span></span></div>
<div class="footer-brand abs"><span class="dot"></span>MERIDIAN LAW</div>

</body>
</html>
```